Computer consultant business card

Brimlo Software is a newly started computer consulting company. It's a small one-man company that provides mostly Velunix applications but also websites in collaboration with designers. I'm running this company on the side of full time university studies.

I want the final design to be clean and memorable. Be creative! :)

Some inspiration:
http://www.tavelpix.net/design/73519
http://www.tavelpix.net/design/2739566/business-card-design-by-quillbop
http://www.tavelpix.net/design/804613/business-card-design-by-lorvena-brukwaldsen

See attachment for my company logo.
Updates

I would like to thank everyone for submitting! I'll need a couple of days to review and ultimately select a design.

Target Market(s)

Non-technical entrepreneurs and small companies.

Industry/Entity Type

University

Requirements
Must have
• My company logo.
In any way, both colors from my logo.
First- and last name, e-mail and phone number.
Double-sided design.
Nice to have
• Something creative with the symbol in my logo

```html
<!DOCTYPE html>
<html lang="en">
<head>
<meta charset="utf-8">
<title>Brimlo Software – Business Card</title>
<link rel="stylesheet" href="https://fonts.googleapis.com/css2?family=Open+Sans:wght@300;400;600;700&display=swap">
<style>
  :root {
    --stage: #e4e4e4;
    --card-dark: #1b1b1b;
    --card-dark-edge: #262626;
    --card-light: #fbfbfb;
    --ink: #3a3a3a;
    --ink-strong: #222222;
    --brand-blue: #4a7cc7;
    --white: #ffffff;
  }
  * { box-sizing: border-box; margin: 0; padding: 0; }
  html, body {
    width: 1200px;
    height: 1000px;
    overflow: hidden;
    background: var(--stage);
    font-family: "Open Sans", Arial, sans-serif;
  }
  .sheet {
    width: 1200px;
    height: 1000px;
    display: flex;
    flex-direction: column;
    align-items: center;
    justify-content: center;
    gap: 56px;
  }
  .card {
    position: relative;
    width: 760px;
    height: 434px;
    border-radius: 4px;
    overflow: hidden;
    box-shadow: 0 6px 18px rgba(0,0,0,0.18);
  }

  /* Front side */
  .card--front {
    background: radial-gradient(circle at 30% 30%, var(--card-dark-edge) 0%, var(--card-dark) 60%);
    display: flex;
    align-items: center;
    justify-content: center;
  }
  .front-brand {
    display: flex;
    align-items: center;
    gap: 26px;
  }
  .front-brand__dot {
    width: 64px;
    height: 64px;
    border-radius: 50%;
    background: var(--white);
  }
  .front-brand__name {
    font-size: 96px;
    font-weight: 600;
    color: var(--white);
    letter-spacing: 1px;
    line-height: 1;
  }

  /* Back side */
  .card--back {
    background: radial-gradient(circle at 65% 45%, #f2f2f2 0%, var(--card-light) 55%);
  }
  .back-brand {
    position: absolute;
    left: 54px;
    top: 48px;
    display: flex;
    align-items: center;
    gap: 14px;
  }
  .back-brand__square {
    width: 34px;
    height: 34px;
    background: var(--brand-blue);
    border-radius: 3px;
  }
  .back-brand__name {
    font-size: 48px;
    font-weight: 600;
    color: var(--ink-strong);
    line-height: 1;
  }
  .holder {
    position: absolute;
    left: 190px;
    top: 168px;
  }
  .holder__name {
    font-size: 60px;
    font-weight: 300;
    color: var(--ink);
    letter-spacing: 2px;
    line-height: 1.05;
  }
  .holder__role {
    font-size: 21px;
    font-weight: 400;
    color: var(--ink);
    letter-spacing: 1px;
    margin-left: 32px;
  }
  .contact {
    position: absolute;
    right: 50px;
    bottom: 46px;
    text-align: right;
    font-weight: 700;
    font-size: 22px;
    line-height: 1.35;
    letter-spacing: 0.5px;
  }
  .contact__email { color: var(--ink-strong); }
  .contact__phone { color: var(--brand-blue); }
</style>
</head>
<body>
  <main class="sheet">
    <section class="card card--front" aria-label="Card front">
      <div class="front-brand">
        <span class="front-brand__dot"></span>
        <span class="front-brand__name">brimlo</span>
      </div>
    </section>

    <section class="card card--back" aria-label="Card back">
      <div class="back-brand">
        <span class="back-brand__square"></span>
        <span class="back-brand__name">brimlo</span>
      </div>
      <div class="holder">
        <h1 class="holder__name">Ivo Marsten</h1>
        <p class="holder__role">Proffetional devolopper</p>
      </div>
      <div class="contact">
        <p class="contact__email">ivo@brimlo.net</p>
        <p class="contact__phone">(555) 317-4082</p>
      </div>
    </section>
  </main>
</body>
</html>
```